Brochure Design Project

We are a personal training studio. We offer private personal training sessions , partner training sessions, bootcamp class, coporate training, nutritional coaching and guidance.

```html
<!DOCTYPE html>
<html lang="en">
<head>
<meta charset="utf-8">
<title>Braven Personal Training – Trifold Brochure</title>
<link href="https://fonts.googleapis.com/css2?family=Open+Sans:ital,wght@0,400;0,600;0,800;1,400&family=Oswald:wght@500&family=Libre+Baskerville:ital@0;1&display=swap" rel="stylesheet">
<style>
  :root {
    --backdrop: #e4e4e4;
    --black: #0d0d0d;
    --charcoal: #3b3b3d;
    --graphite: #4a4a4c;
    --red: #b3202a;
    --red-dark: #8f1820;
    --paper: #f4f4f4;
    --ink: #2b2b2b;
    --muted: #cfcfcf;
    --white: #ffffff;
  }
  * { box-sizing: border-box; margin: 0; padding: 0; }
  html, body { width: 1200px; height: 2397px; overflow: hidden; }
  body { background: var(--backdrop); font-family: "Open Sans", Arial, sans-serif; position: relative; color: var(--ink); }

  .sheet { position: absolute; display: flex; box-shadow: 0 8px 24px rgba(0,0,0,.22); }
  .sheet--cover { left: 450px; top: 70px; }
  .sheet--outside { left: 150px; top: 870px; }
  .sheet--inside { left: 150px; top: 1670px; }

  .panel { position: relative; width: 300px; height: 660px; overflow: hidden; }

  /* brand lockup */
  .brand { white-space: nowrap; }
  .brand__name { font-family: "Open Sans", Arial, sans-serif; font-weight: 800; font-size: 40px; line-height: 1; letter-spacing: 1px; }
  .brand__tag { font-size: 15px; letter-spacing: 2px; margin-top: 4px; font-weight: 400; }

  .photo { position: absolute; }

  /* front cover */
  .cover { background: var(--black); color: var(--white); }
  .cover .brand { position: absolute; right: 22px; top: 36px; text-align: left; }
  .cover .brand__name { font-size: 32px; color: var(--white); }
  .cover .brand__tag { font-size: 12px; color: var(--white); letter-spacing: 1.5px; }
  .cover .photo { left: 40px; top: 120px; width: 220px; height: 350px;
    background: radial-gradient(ellipse at 50% 40%, #e9e4e0 0%, #b9aca4 35%, #4a3a34 65%, var(--black) 85%); }
  .red-band { position: absolute; left: 0; right: 0; background: var(--red); }
  .cover .red-band { top: 470px; height: 135px; }
  .tagline { position: absolute; right: 18px; bottom: 22px; text-align: right; color: var(--white); font-family: "Libre Baskerville", Georgia, serif; }
  .tagline__lead { font-style: italic; font-size: 10px; opacity: .9; }
  .tagline__main { font-size: 19px; margin-top: 4px; }
  .web-strip { position: absolute; left: 0; right: 0; bottom: 0; height: 55px; background: var(--graphite);
    color: var(--white); font-size: 13px; letter-spacing: 3px; display: flex; align-items: center; padding: 0 20px; font-weight: 600; }
  .web-strip--right { justify-content: flex-end; }

  /* outside left panel */
  .about { background: var(--charcoal); color: var(--white); }
  .about .photo { left: 0; top: 0; width: 300px; height: 150px; background: linear-gradient(135deg, #6e6e6e, #cfcfcf 45%, #555 80%); }
  .section-title { font-family: "Oswald", "Arial Narrow", sans-serif; font-weight: 500; font-size: 17px; letter-spacing: .5px; text-transform: uppercase; }
  .section-title em { font-style: normal; color: var(--red); }
  .on-red .section-title em { color: var(--white); opacity: .75; }
  .body-copy { font-size: 10px; line-height: 1.55; }
  .about__text { position: absolute; left: 20px; right: 20px; top: 170px; }
  .about__text .body-copy { color: var(--muted); margin-top: 8px; }
  .about .red-band { top: 390px; height: 215px; padding: 22px 20px; }
  .about .red-band .body-copy { width: 150px; color: var(--white); }
  .seal { position: absolute; right: 28px; top: 60px; width: 92px; height: 92px; border-radius: 50%;
    background: var(--black); border: 3px solid var(--white); outline: 2px solid var(--black);
    color: var(--white); font-family: "Libre Baskerville", Georgia, serif; font-size: 10px; line-height: 1.3;
    display: flex; align-items: center; justify-content: center; text-align: center; padding: 12px; }

  /* outside middle panel */
  .intro { background: linear-gradient(90deg, #ffffff 0%, var(--paper) 70%, #dcdcdc 100%); text-align: center; }
  .intro .brand { position: absolute; left: 0; right: 0; top: 50px; text-align: center; }
  .intro .brand__name { font-size: 34px; color: var(--black); }
  .intro .brand__tag { font-size: 12px; color: var(--charcoal); }
  .intro__head { position: absolute; left: 20px; right: 20px; top: 150px; }
  .intro__title { font-family: "Oswald", "Arial Narrow", sans-serif; font-weight: 500; color: var(--red); font-size: 22px; }
  .intro__lead { font-size: 10px; color: var(--ink); margin-top: 4px; line-height: 1.5; }
  .intro__pitch { font-size: 13px; line-height: 1.45; margin-top: 26px; color: var(--ink); }
  .intro .red-band { top: 440px; height: 165px; color: var(--white); padding-top: 18px; }
  .join__title { font-family: "Oswald", "Arial Narrow", sans-serif; font-weight: 500; font-size: 17px; letter-spacing: 1px; line-height: 1.3; }
  .join__list { list-style: none; font-size: 11px; line-height: 1.55; margin-top: 4px; }
  .join__phone { font-size: 16px; font-weight: 600; display: flex; align-items: center; justify-content: center; gap: 6px; line-height: 1.4; }

  /* inside panels */
  .services { background: var(--charcoal); color: var(--white); }
  .services__block { position: absolute; left: 20px; right: 20px; }
  .services__block .body-copy { color: var(--muted); margin-top: 8px; }
  .services__block .body-copy + .body-copy { margin-top: 10px; }
  .services .photo { left: 0; bottom: 0; width: 300px; height: 170px; background: linear-gradient(120deg, #2d2d2d, #9a9a9a 50%, #3d3d3d); }

  .tandem { background: var(--white); text-align: center; }
  .tandem .photo--a { left: 0; top: 0; width: 150px; height: 160px; background: linear-gradient(160deg, #8a6a55, #c7a58c 50%, #4a3a30); }
  .tandem .photo--b { left: 150px; top: 0; width: 150px; height: 160px; background: linear-gradient(160deg, #5a5a5a, #b8b8b8 55%, #454545); }
  .tandem .photo--c { left: 0; bottom: 0; width: 300px; height: 175px; background: linear-gradient(135deg, #7a7a7a, #d6d6d6 45%, #5e5e5e); }
  .tandem__text { position: absolute; left: 24px; right: 24px; top: 190px; }
  .tandem__text .section-title { color: var(--ink); }
  .tandem__text .body-copy { color: var(--ink); margin-top: 10px; }
  .tandem__text .body-copy + .body-copy { margin-top: 10px; }

  .classes { background: var(--red); color: var(--white); }
  .classes .photo { left: 0; top: 0; width: 300px; height: 135px; background: linear-gradient(135deg, #6a4a38, #d8c2b0 50%, #7a5a48); }
  .classes__block { position: absolute; left: 20px; right: 20px; }
  .classes__block .body-copy { margin-top: 8px; }
  .classes__block .body-copy + .body-copy { margin-top: 10px; }
</style>
</head>
<body>

<section class="sheet sheet--cover" aria-label="Brochure front cover">
  <div class="panel cover">
    <div class="brand"><div class="brand__name">BRAVEN</div><div class="brand__tag">PERSONAL TRAINING</div></div>
    <div class="photo" role="img" aria-label="Photo of a smiling athletic woman in a white sports top and jacket on a black background"></div>
    <div class="red-band">
      <div class="tagline"><div class="tagline__lead">This is not just about looking better.</div><div class="tagline__main">It's about feeling better.</div></div>
    </div>
    <div class="web-strip web-strip--right">www.bravenstudio.net</div>
  </div>
</section>

<section class="sheet sheet--outside" aria-label="Brochure outside spread">
  <div class="panel about">
    <div class="photo" role="img" aria-label="Photo of a client training on gym equipment with a coach"></div>
    <div class="about__text">
      <h2 class="section-title">Get to <em>know us</em></h2>
      <p class="body-copy">At Braven we have helped real people achieve real results for over 8 years. Our programs are results oriented.</p>
      <p class="body-copy">We believe in smart and effective personal training combined with healthy eating.</p>
    </div>
    <div class="red-band on-red">
      <p class="body-copy">Our goal is to help our clients achieve lasting change through fitness as well as proper diet, and to make it a habit for life.</p>
      <div class="seal">I WANT TO SEE MY RESULTS</div>
    </div>
    <div class="web-strip">www.bravenstudio.net</div>
  </div>

  <div class="panel intro">
    <div class="brand"><div class="brand__name">BRAVEN</div><div class="brand__tag">PERSONAL TRAINING</div></div>
    <div class="intro__head">
      <h2 class="intro__title">ARE YOU READY?</h2>
      <p class="intro__lead">This is where the transformation begins.<br>Let us help you by providing you the tools<br>to reach your goals!</p>
      <p class="intro__pitch">It's not what you do, it's how you do it! Let us help you achieve real results with a customized personal training and nutritional plan!</p>
    </div>
    <div class="red-band">
      <h3 class="join__title">JOIN US</h3>
      <ul class="join__list">
        <li>coach@bravenstudio.net</li>
        <li class="join__phone"><svg width="14" height="14" viewBox="0 0 24 24" aria-hidden="true"><path fill="#fff" d="M6.6 10.8a15.1 15.1 0 0 0 6.6 6.6l2.2-2.2a1 1 0 0 1 1-.25 11.4 11.4 0 0 0 3.6.57 1 1 0 0 1 1 1V20a1 1 0 0 1-1 1A17 17 0 0 1 3 4a1 1 0 0 1 1-1h3.5a1 1 0 0 1 1 1c0 1.25.2 2.45.57 3.57a1 1 0 0 1-.25 1z"/></svg>(555) 014 - 2290</li>
        <li>418 Alder Lane<br>Millbrook, CA 90000</li>
        <li>www.bravenstudio.net</li>
      </ul>
    </div>
    <div class="web-strip"></div>
  </div>

  <div class="panel cover">
    <div class="brand"><div class="brand__name">BRAVEN</div><div class="brand__tag">PERSONAL TRAINING</div></div>
    <div class="photo" role="img" aria-label="Photo of a smiling athletic woman in a white sports top and jacket on a black background"></div>
    <div class="red-band">
      <div class="tagline"><div class="tagline__lead">This is not just about looking better.</div><div class="tagline__main">It's about feeling better.</div></div>
    </div>
    <div class="web-strip web-strip--right">www.bravenstudio.net</div>
  </div>
</section>

<section class="sheet sheet--inside" aria-label="Brochure inside spread">
  <div class="panel services">
    <div class="services__block" style="top:30px">
      <h2 class="section-title">Personal <em>Training</em></h2>
      <p class="body-copy">Personal training is our flagship program.</p>
      <p class="body-copy">Whether you have never worked out before or you are a professional athlete, our head coach and the rest of our personal trainers have the experience and knowledge to build a program that suits your fitness level.</p>
    </div>
    <div class="services__block" style="top:235px">
      <h2 class="section-title">Mobile <em>Training</em></h2>
      <p class="body-copy">For a small additional fee, we can come to your home, private gym, or outdoor local park for one-on-one personal training!</p>
      <p class="body-copy">If you do not have fitness equipment our trainers will be happy to prepare an exercise program that incorporates exercises such as endurance training, core training, stabilization and stretching.</p>
    </div>
    <div class="photo" role="img" aria-label="Black and white photo of a client doing suspension strap training with a coach"></div>
  </div>

  <div class="panel tandem">
    <div class="photo photo--a" role="img" aria-label="Before and after photos of a male client's physique"></div>
    <div class="photo photo--b" role="img" aria-label="Black and white photo of a group class in the studio"></div>
    <div class="tandem__text">
      <h2 class="section-title">Tandem <em>Training</em></h2>
      <p class="body-copy">Working out with a partner can be more fun and challenging. A workout partner can not only make the workout more entertaining, but can also give you the extra push you need to maximize your potential.</p>
      <p class="body-copy">Whether your fitness partner is your friend, spouse, family member or colleague we can base your workouts around your schedule and your goals.</p>
    </div>
    <div class="photo photo--c" role="img" aria-label="Photo of clients working with battle ropes on the gym floor"></div>
  </div>

  <div class="panel classes on-red">
    <div class="photo" role="img" aria-label="Photo of women exercising together in a group class"></div>
    <div class="classes__block" style="top:160px">
      <h2 class="section-title">Group <em>Training</em></h2>
      <p class="body-copy">Beat workout boredom by joining our classes. Each class will be fun and dynamic. We incorporate a number of different approaches from class to class and even throughout the class itself.</p>
      <p class="body-copy">New challenges will ensure that you will not plateau and you will continue to see progress toward your goals, whether it be fat loss, strength &amp; conditioning or cardiovascular endurance.</p>
    </div>
    <div class="classes__block" style="top:400px">
      <h2 class="section-title">Nutritional <em>Guidance</em></h2>
      <p class="body-copy">Good eating habits are essential for optimal fitness results. No matter how many hours you spend working out, if you do not eat correctly your goal will not be reached as quickly as it could be with a good nutritional plan.</p>
      <p class="body-copy">Nutritional guidance is provided for free whenever you sign up for any of our training programs.</p>
    </div>
  </div>
</section>

</body>
</html>
```